Painting Company Business Card

Brightwell Painting needs a new business card. See attachments for our logo and current card as an example.
We want to utilize the same colors in the logo, and keep all the information that is currently on it. Just need an updated and modern design.
We are open to loosing the Association Logos if it means a better design.
We are also entertaining a spot for a picture of a headshot of the person listed on the card. Head shot can be finished later.

```html
<!DOCTYPE html>
<html lang="en">
<head>
<meta charset="utf-8">
<title>Brightwell Painting – Business Card</title>
<link rel="stylesheet" href="https://fonts.googleapis.com/css2?family=Arimo:wght@400;700&display=swap">
<style>
  :root {
    --green: #2f4a22;
    --maroon: #5b2a2c;
    --ink: #111111;
    --paper: #ffffff;
    --badge-blue: #1f4f8c;
    --badge-red: #c8272e;
    --badge-grey: #6d6d6d;
  }
  * { box-sizing: border-box; margin: 0; padding: 0; }
  html, body {
    width: 1200px; height: 1000px; overflow: hidden;
    background: var(--paper);
    font-family: "Arimo", Arial, sans-serif;
  }
  .canvas { position: relative; width: 1200px; height: 1000px; }

  .card {
    position: absolute; left: 222px; width: 748px; height: 427px;
    border: 2.5px solid var(--ink); border-radius: 24px;
    background: var(--paper);
  }
  .card--front { top: 44px; }
  .card--back { top: 535px; }

  .brand {
    position: absolute; display: flex; align-items: center; gap: 12px;
    color: var(--green); font-weight: 700; line-height: 1.02;
  }
  .brand__mark { width: 18px; height: 70px; background: var(--maroon); flex: none; }
  .card--front .brand { left: 28px; top: 30px; font-size: 34px; }
  .card--back .brand { left: 30px; top: 30px; font-size: 40px; }

  .person { position: absolute; right: 48px; top: 34px; text-align: right; font-weight: 700; }
  .person__name { color: var(--green); font-size: 44px; line-height: 1.1; }
  .person__role { color: var(--maroon); font-size: 26px; margin-top: 2px; }

  .contact-icons { position: absolute; left: 200px; top: 216px; }

  .contact {
    position: absolute; left: 0; right: 0; top: 266px;
    text-align: center; color: var(--maroon); font-weight: 700;
    font-size: 26px; line-height: 36px; list-style: none;
    padding-left: 0; transform: translateX(-4px);
  }

  .services {
    position: absolute; left: 34px; top: 162px; list-style: none;
    color: var(--green); font-weight: 700; font-size: 26px;
  }
  .services__item { display: flex; align-items: center; height: 50px; }
  .services__tick { width: 46px; height: 42px; margin-right: 30px; flex: none; }

  .badges { position: absolute; left: 490px; top: 62px; }
</style>
</head>
<body>
<div class="canvas">

  <section class="card card--front">
    <div class="brand">
      <span class="brand__mark"></span>
      <span class="brand__name">Brightwell<br>Painting</span>
    </div>

    <div class="person">
      <p class="person__name">Daniel Harper</p>
      <p class="person__role">Qualily Manager</p>
    </div>

    <svg class="contact-icons" width="330" height="38" viewBox="0 0 330 38" aria-hidden="true">
      <g fill="var(--green)" stroke="var(--green)">
        <path d="M4 19 L64 19" stroke-width="3"/>
        <path d="M4 13 L14 19 L4 25 Z"/>
        <path d="M70 19 L56 12 L56 26 Z"/>
        <path d="M326 19 L266 19" stroke-width="3"/>
        <path d="M326 13 L316 19 L326 25 Z"/>
        <path d="M260 19 L274 12 L274 26 Z"/>
        <!-- phone -->
        <path d="M103 9 h34 a4 4 0 0 1 4 4 v4 h-8 v-4 h-26 v4 h-8 v-4 a4 4 0 0 1 4 -4 Z" stroke="none"/>
        <rect x="104" y="17" width="32" height="15" rx="2" stroke="none"/>
        <circle cx="120" cy="24" r="4" fill="var(--paper)" stroke="none"/>
      </g>
      <g fill="none" stroke="var(--green)" stroke-width="2">
        <rect x="149" y="9" width="34" height="22"/>
        <path d="M149 9 L166 22 L183 9 M149 31 L161 19 M183 31 L171 19"/>
        <circle cx="210" cy="20" r="14"/>
        <ellipse cx="210" cy="20" rx="6" ry="14"/>
        <path d="M196 20 H224 M199 12 H221 M199 28 H221 M210 6 V34"/>
      </g>
    </svg>

    <ul class="contact">
      <li>262-555-0147</li>
      <li>Daniel.Harper@brightmail.com</li>
      <li>BrightwellPainting.com</li>
    </ul>
  </section>

  <section class="card card--back">
    <div class="brand">
      <span class="brand__mark"></span>
      <span class="brand__name">Brightwell<br>Painting</span>
    </div>

    <ul class="services">
      <li class="services__item">
        <svg class="services__tick" viewBox="0 0 46 42" aria-hidden="true"><rect x="2" y="10" width="30" height="30" fill="none" stroke="var(--maroon)" stroke-width="2.5"/><path d="M8 22 L17 33 L43 3" fill="none" stroke="var(--maroon)" stroke-width="7" stroke-linejoin="round"/></svg>
        Exterior Painting
      </li>
      <li class="services__item">
        <svg class="services__tick" viewBox="0 0 46 42" aria-hidden="true"><rect x="2" y="10" width="30" height="30" fill="none" stroke="var(--maroon)" stroke-width="2.5"/><path d="M8 22 L17 33 L43 3" fill="none" stroke="var(--maroon)" stroke-width="7" stroke-linejoin="round"/></svg>
        Interion Painting
      </li>
      <li class="services__item">
        <svg class="services__tick" viewBox="0 0 46 42" aria-hidden="true"><rect x="2" y="10" width="30" height="30" fill="none" stroke="var(--maroon)" stroke-width="2.5"/><path d="M8 22 L17 33 L43 3" fill="none" stroke="var(--maroon)" stroke-width="7" stroke-linejoin="round"/></svg>
        Carpentry
      </li>
      <li class="services__item">
        <svg class="services__tick" viewBox="0 0 46 42" aria-hidden="true"><rect x="2" y="10" width="30" height="30" fill="none" stroke="var(--maroon)" stroke-width="2.5"/><path d="M8 22 L17 33 L43 3" fill="none" stroke="var(--maroon)" stroke-width="7" stroke-linejoin="round"/></svg>
        Drywall
      </li>
    </ul>

    <svg class="badges" width="230" height="265" viewBox="0 0 230 265" role="img" aria-label="Trade association and accreditation badges">
      <rect x="4" y="4" width="76" height="129" rx="5" fill="var(--badge-blue)"/>
      <rect x="88" y="4" width="130" height="64" rx="3" fill="var(--badge-red)"/>
      <rect x="110" y="70" width="84" height="62" rx="3" fill="var(--badge-blue)" opacity="0.55"/>
      <rect x="10" y="142" width="74" height="122" rx="3" fill="var(--badge-grey)" opacity="0.7"/>
      <rect x="86" y="146" width="142" height="56" rx="6" fill="var(--badge-blue)" opacity="0.8"/>
      <rect x="116" y="206" width="84" height="57" rx="3" fill="var(--badge-red)" opacity="0.85"/>
    </svg>
  </section>

</div>
</body>
</html>
```